Roadward Lane Management Company Website

Modern website Wordpress design using all greyscale photos with a pop of red (such as road closure signs or detour cones) for strategic emphasis. (see brand guide for color codes)
The creative goal is to leverage high-contrast, desaturated imagery to create a clean, professional, and industrial feel. The selective use of red will draw immediate attention to critical elements—such as road hazards, safety equipment, or key messages to ensure the viewer's focus is directed with purpose.

Brand guide, homepage content and logo are attached. Create clean professional user experience to market services to industry professionals.

```html
<!DOCTYPE html>
<html lang="en">
<head>
<meta charset="utf-8">
<title>Roadward Lane Management Company</title>
<link href="https://fonts.googleapis.com/css2?family=Archivo:wdth,wght@62..125,400..900&family=Inter:wght@400;500;600&display=swap" rel="stylesheet">
<style>
:root{
  --red:#e8232a;
  --red-deep:#b91c22;
  --ink:#2b2b2b;
  --ink-soft:#4a4a4a;
  --muted:#7a7a7a;
  --hero-bg:#e6e6e6;
  --panel:#f3f3f3;
  --section:#f4f4f4;
  --card:#ffffff;
  --why-bg:#eeeeee;
  --why-card:#f8f8f8;
  --dark:#0d0d0d;
  --line:#d6d6d6;
}
*{box-sizing:border-box;margin:0;padding:0}
html,body{width:1200px;height:3205px;overflow:hidden}
body{font-family:"Inter",Arial,sans-serif;color:var(--ink);background:#fff;position:relative}
.abs{position:absolute}
.display{font-family:"Archivo",Arial,sans-serif;font-stretch:118%;font-weight:800}

/* header */
.site-header{position:absolute;left:0;top:0;width:1200px;height:65px;background:#fff;border-bottom:1px solid #e4e4e4}
.brand{position:absolute;left:144px;top:20px;display:flex;align-items:center;gap:8px;font-family:"Archivo",sans-serif;font-stretch:118%;font-weight:800;font-size:21px;color:var(--ink)}
.brand-mark{width:14px;height:14px;background:var(--red)}
.main-nav{position:absolute;right:144px;top:20px;display:flex;align-items:center;gap:30px;font-size:11px;color:var(--ink-soft)}
.main-nav .active{color:var(--red);position:relative}
.main-nav .active::after{content:"";position:absolute;left:-8px;right:-8px;bottom:-11px;height:2px;background:var(--red)}
.nav-cta{background:#3a3a3a;color:#fff;padding:7px 13px;border-radius:2px}

/* hero */
.hero{position:absolute;left:0;top:65px;width:1200px;height:1031px;background:var(--hero-bg)}
.hero h1{position:absolute;left:0;top:48px;width:1200px;text-align:center;font-size:50px;line-height:55px;color:#333}
.hero h1 em{font-style:normal;color:var(--red)}
.hero-lede{position:absolute;left:0;top:172px;width:1200px;text-align:center;font-size:14.5px;line-height:21px;color:#3a3a3a}
.hero-actions{position:absolute;left:0;top:237px;width:1200px;display:flex;justify-content:center;gap:19px}
.btn{font-family:"Archivo",sans-serif;font-weight:600;font-size:12px;padding:6px 13px;border-radius:2px;color:#fff}
.btn-red{background:var(--red)}
.btn-dark{background:#3b3b3b}
.photo-frame{position:absolute;background:#fff;border-radius:14px;padding:4px;box-shadow:0 2px 8px rgba(0,0,0,.12)}
.photo{width:100%;height:100%;border-radius:11px}

/* photo tones: greyscale with the red accent each scene carries */
.tone-cones{background:linear-gradient(115deg,#6f6f6f 0%,#b9b9b9 22%,#d8572f 38%,#c9c9c9 55%,#8d8d8d 75%,#3d3d3d 100%)}
.tone-truck{background:linear-gradient(100deg,#c8262b 0%,#d9383a 22%,#9a9a9a 40%,#e4e4e4 62%,#a3a3a3 80%,#4e4e4e 100%)}
.tone-stop{background:linear-gradient(135deg,#3f3f3f 0%,#8a8a8a 30%,#d93a34 55%,#b4b4b4 72%,#4a4a4a 100%)}
.tone-access{background:linear-gradient(160deg,#4b4b4b 0%,#7c7c7c 35%,#d33a36 58%,#9b9b9b 78%,#5c5c5c 100%)}
.tone-roadwork{background:linear-gradient(170deg,#cfcfcf 0%,#a8a8a8 30%,#e4571f 50%,#8c8c8c 72%,#5e5e5e 100%)}
.tone-attenuator{background:linear-gradient(150deg,#6a6a6a 0%,#a4a4a4 30%,#c9342f 58%,#757575 78%,#3a3a3a 100%)}
.tone-highway{background:linear-gradient(165deg,#e2e2e2 0%,#b6b6b6 35%,#e26a2d 55%,#9a9a9a 75%,#6b6b6b 100%)}
.tone-detour{background:linear-gradient(160deg,#474747 0%,#8f8f8f 35%,#e0562a 58%,#6a6a6a 80%,#2f2f2f 100%)}
.tone-slow{background:linear-gradient(135deg,#e08a1e 0%,#b7b7b7 35%,#dcdcdc 55%,#7e7e7e 80%,#444 100%)}
.tone-event{background:linear-gradient(150deg,#9a9a9a 0%,#5e5e5e 35%,#d8572a 58%,#6f6f6f 78%,#3a3a3a 100%)}
.tone-lanes{background:linear-gradient(115deg,#8a8a8a 0%,#c3c3c3 25%,#e4501f 45%,#a7a7a7 65%,#5a5a5a 100%)}

.safety-panel{position:absolute;left:0;top:737px;width:609px;height:229px;background:var(--panel)}
.stripe-block{position:absolute;background:linear-gradient(90deg,var(--red),var(--red-deep))}
.safety-title{position:absolute;left:144px;top:859px;font-size:24px;line-height:28px;color:#333}
.safety-copy{position:absolute;left:634px;top:804px;width:412px;font-size:17px;line-height:25px;color:#3a3a3a}

/* services */
.services{position:absolute;left:0;top:1096px;width:1200px;height:1098px;background:var(--section)}
.eyebrow{font-family:"Archivo",sans-serif;font-stretch:110%;font-weight:600;font-size:17px;color:#333}
.section-title{font-size:37px;line-height:40px;color:var(--red)}
.learn-more{position:absolute;right:144px;top:70px;font-family:"Archivo",sans-serif;font-stretch:110%;font-weight:600;font-size:15px;color:#333;display:flex;align-items:center;gap:8px}
.divider{position:absolute;left:144px;top:115px;width:912px;height:1px;background:var(--line)}
.service-card{position:absolute;width:292px;height:274px;background:var(--card);padding:10px}
.service-card .photo{height:187px;border-radius:0}
.service-card h3{margin-top:14px;font-size:12px;font-weight:500;color:#333;display:flex;justify-content:space-between;align-items:center;white-space:nowrap}
.service-card p{margin-top:8px;font-size:9.5px;line-height:15px;color:var(--muted);padding-right:24px}

/* region */
.region{position:absolute;left:0;top:2194px;width:1200px;height:462px;background:linear-gradient(100deg,#2c2c2c 0%,#505050 30%,#2a2a2a 55%,#4a2c2b 78%,#3a3a3a 100%)}
.map-area{position:absolute;left:199px;top:72px;width:324px;height:330px;background:linear-gradient(160deg,var(--red),var(--red-deep));border-radius:6px}
.region h2{position:absolute;left:625px;top:109px;width:400px;font-size:24px;line-height:27px;color:#fff}
.region ul{position:absolute;left:625px;top:221px;list-style:none}
.region li{display:flex;align-items:center;gap:14px;height:35px;font-size:12.5px;color:#fff}

/* why */
.why{position:absolute;left:0;top:2656px;width:1200px;height:357px;background:var(--why-bg)}
.why-grid{position:absolute;left:144px;top:148px;width:912px;height:147px;display:grid;grid-template-columns:repeat(4,1fr);gap:1px}
.why-card{background:var(--why-card);padding:22px 18px}
.why-card h3{margin-top:14px;font-size:12px;font-weight:500;color:#333;white-space:nowrap}
.why-card p{margin-top:10px;font-size:9.5px;line-height:14px;color:#555}

/* footer */
.site-footer{position:absolute;left:0;top:3013px;width:1200px;height:192px;background:var(--dark)}
.site-footer .brand{top:50px;color:#fff}
.partner-badge{position:absolute;left:488px;top:44px;width:104px;height:34px;border-radius:4px;background:#2a2a2a;border:1px solid #3a3a3a}
.footer-nav{position:absolute;right:144px;top:58px;display:flex;gap:20px;font-size:10.5px;color:#fff}
.footer-line{position:absolute;left:144px;top:130px;width:912px;height:1px;background:#333}
.copyright{position:absolute;left:144px;top:153px;font-size:10px;color:#ddd}
.legal{position:absolute;right:144px;top:153px;display:flex;gap:10px;font-size:10px;color:#ddd}
</style>
</head>
<body>

<header class="site-header">
  <div class="brand"><span class="brand-mark"></span>Roadward</div>
  <nav class="main-nav">
    <span class="active">Home</span><span>About</span><span>Services</span><span>Rentals</span><span>Jobs</span>
    <span class="nav-cta">Contact</span>
  </nav>
</header>

<section class="hero">
  <h1 class="display">Traffic Control Solutions<br>Engineered for <em>Safety</em></h1>
  <p class="hero-lede">We ensure safe, efficient traffic management for construction zones, detours, and events<br>with expert planning, clear communication, and top-tier service</p>
  <div class="hero-actions"><span class="btn btn-red">Get a Quote</span><span class="btn btn-dark">Learn more</span></div>

  <div class="photo-frame" style="left:21px;top:288px;width:347px;height:333px"><div class="photo tone-cones" role="img" aria-label="Greyscale photo of a highway lane lined with orange and white traffic cones"></div></div>
  <div class="photo-frame" style="left:383px;top:333px;width:434px;height:324px"><div class="photo tone-truck" role="img" aria-label="Greyscale photo of a company work truck loaded with red barricades"></div></div>
  <div class="photo-frame" style="left:833px;top:288px;width:347px;height:333px"><div class="photo tone-stop" role="img" aria-label="Greyscale photo of a flagger in a hard hat holding a red stop paddle"></div></div>

  <div class="safety-panel"></div>
  <div class="stripe-block" style="left:144px;top:788px;width:212px;height:50px" role="img" aria-label="Red and black hazard chevron stripe"></div>
  <div class="safety-title display">Safety isn’t a priority It’s the<br>Foundation of everything we do</div>
  <p class="safety-copy">We don’t just follow safety standards - We set them. Our experienced team ensures every project is compliant with DOT and federal safety regulations while keeping workers and drivers safe.</p>
</section>

<section class="services">
  <div class="abs" style="left:144px;top:45px">
    <div class="eyebrow">Our</div>
    <div class="section-title display">Services</div>
  </div>
  <div class="learn-more">Learn More
    <svg width="14" height="12" viewBox="0 0 14 12" fill="none" stroke="#333" stroke-width="1.5"><path d="M1 6h11M7 1l5 5-5 5"/></svg>
  </div>
  <div class="divider"></div>

  <article class="service-card" style="left:144px;top:150px"><div class="photo tone-stop" role="img" aria-label="Flagger holding a red stop sign beside traffic"></div><h3>Flagging &amp; Lane Closures<svg width="9" height="9" viewBox="0 0 9 9" fill="none" stroke="#333" stroke-width="1.2"><path d="M1 8l7-7M3 1h5v5"/></svg></h3><p>Professional flaggers ensuring smooth and safe road operations.</p></article>
  <article class="service-card" style="left:454px;top:150px"><div class="photo tone-access" role="img" aria-label="Red access only sign on a barricade with cones"></div><h3>Temporary Traffic Control Plans (TTCPs)<svg width="9" height="9" viewBox="0 0 9 9" fill="none" stroke="#333" stroke-width="1.2"><path d="M1 8l7-7M3 1h5v5"/></svg></h3><p>Custom plans designed for compliance and efficiency.</p></article>
  <article class="service-card" style="left:763px;top:150px"><div class="photo tone-roadwork" role="img" aria-label="Orange road work ahead sign beside a row of drums"></div><h3>Signage &amp; Barricades<svg width="9" height="9" viewBox="0 0 9 9" fill="none" stroke="#333" stroke-width="1.2"><path d="M1 8l7-7M3 1h5v5"/></svg></h3><p>High-visibility signs and barriers for work zones and detours.</p></article>

  <article class="service-card" style="left:144px;top:450px"><div class="photo tone-attenuator" role="img" aria-label="Truck-mounted crash attenuator with red chevrons on a highway"></div><h3>Crash Attenuators &amp; TMAs<svg width="9" height="9" viewBox="0 0 9 9" fill="none" stroke="#333" stroke-width="1.2"><path d="M1 8l7-7M3 1h5v5"/></svg></h3><p>Vehicle-mounted safety equipment to reduce impact risks.</p></article>
  <article class="service-card" style="left:454px;top:450px"><div class="photo tone-highway" role="img" aria-label="Arrow board trailer and cone taper on a highway shoulder"></div><h3>Heavy Highway Traffic Control<svg width="9" height="9" viewBox="0 0 9 9" fill="none" stroke="#333" stroke-width="1.2"><path d="M1 8l7-7M3 1h5v5"/></svg></h3><p>Solutions for major road construction and maintenance projects.</p></article>
  <article class="service-card" style="left:763px;top:450px"><div class="photo tone-detour" role="img" aria-label="Road closed barricade with detour sign and cones on a city street"></div><h3>Roadway Detours &amp; Lane Shifts<svg width="9" height="9" viewBox="0 0 9 9" fill="none" stroke="#333" stroke-width="1.2"><path d="M1 8l7-7M3 1h5v5"/></svg></h3><p>Expert planning and execution of temporary traffic routes.</p></article>

  <article class="service-card" style="left:144px;top:747px"><div class="photo tone-slow" role="img" aria-label="Worker in a hard hat holding an orange slow paddle"></div><h3>Work Zone Safety Consulting<svg width="9" height="9" viewBox="0 0 9 9" fill="none" stroke="#333" stroke-width="1.2"><path d="M1 8l7-7M3 1h5v5"/></svg></h3><p>Vehicle-mounted safety equipment to reduce impact risks.</p></article>
  <article class="service-card" style="left:454px;top:747px"><div class="photo tone-event" role="img" aria-label="Message board reading event traffic left beside city traffic"></div><h3>Event Traffic &amp; Crowd Control<svg width="9" height="9" viewBox="0 0 9 9" fill="none" stroke="#333" stroke-width="1.2"><path d="M1 8l7-7M3 1h5v5"/></svg></h3><p>Solutions for major road construction and maintenance projects.</p></article>
  <article class="service-card" style="left:763px;top:747px"><div class="photo tone-lanes" role="img" aria-label="Row of orange traffic cones separating highway lanes"></div><h3>Roadway Detours &amp; Lane Shifts<svg width="9" height="9" viewBox="0 0 9 9" fill="none" stroke="#333" stroke-width="1.2"><path d="M1 8l7-7M3 1h5v5"/></svg></h3><p>Expert planning and execution of temporary traffic routes.</p></article>
</section>

<section class="region" role="img" aria-label="Darkened photo of a work zone truck and cones on a highway">
  <div class="stripe-block" style="left:987px;top:0;width:213px;height:47px" role="img" aria-label="Red and black hazard chevron stripe"></div>
  <div class="map-area" role="img" aria-label="Red map of the state of Texas"></div>
  <h2 class="display">Serving Texas industry to Ensure Safery, Compliance, and Efficient Traffic Flow</h2>
  <ul>
    <li><svg width="20" height="20" viewBox="0 0 20 20" fill="none" stroke="#fff" stroke-width="1.3"><circle cx="10" cy="10" r="8.5"/><path d="M6 10.3l2.7 2.6L14 7.5"/></svg>Road construction, maintenance &amp; Detours</li>
    <li><svg width="20" height="20" viewBox="0 0 20 20" fill="none" stroke="#fff" stroke-width="1.3"><circle cx="10" cy="10" r="8.5"/><path d="M6 10.3l2.7 2.6L14 7.5"/></svg>Municipal &amp; State projects</li>
    <li><svg width="20" height="20" viewBox="0 0 20 20" fill="none" stroke="#fff" stroke-width="1.3"><circle cx="10" cy="10" r="8.5"/><path d="M6 10.3l2.7 2.6L14 7.5"/></svg>Private Sector &amp; Commercial Contractors</li>
    <li><svg width="20" height="20" viewBox="0 0 20 20" fill="none" stroke="#fff" stroke-width="1.3"><circle cx="10" cy="10" r="8.5"/><path d="M6 10.3l2.7 2.6L14 7.5"/></svg>Oil, Gas, Wind, Solar, &amp; Manufacturing</li>
  </ul>
</section>

<section class="why">
  <div class="abs" style="left:144px;top:52px">
    <div class="eyebrow">Why</div>
    <div class="section-title display">Choose Us</div>
  </div>
  <div class="why-grid">
    <div class="why-card">
      <svg width="30" height="32" viewBox="0 0 30 32" fill="var(--red)"><path d="M6 0h6l3 6 3-6h6l-5 10H11z"/><circle cx="15" cy="20" r="10"/><path d="M15 14l1.8 3.8 4 .4-3 2.8.9 4-3.7-2.1-3.7 2.1.9-4-3-2.8 4-.4z" fill="#fff"/></svg>
      <h3>DOT - Compliant &amp; Certified</h3><p>We follow the highest safety and compliance standards.</p>
    </div>
    <div class="why-card">
      <svg width="30" height="32" viewBox="0 0 30 32" fill="var(--red)"><path d="M3 16a12 12 0 0 1 24 0v2H3z"/><rect x="12" y="3" width="6" height="8" fill="#fff"/><rect x="1" y="18" width="28" height="4" rx="1"/><path d="M7 24h16v2a8 8 0 0 1-16 0z"/></svg>
      <h3>Experienced &amp; Trained Crew</h3><p>Our team is highly skilled in traffic control solutions.</p>
    </div>
    <div class="why-card">
      <svg width="30" height="32" viewBox="0 0 30 32" fill="var(--red)"><path d="M15 1l12 5v9c0 8-5 13-12 16C8 28 3 23 3 15V6z"/><circle cx="15" cy="13" r="3.5" fill="#fff"/><path d="M9 22a6 6 0 0 1 12 0z" fill="#fff"/></svg>
      <h3>Reliable &amp; Responsive</h3><p>We prioritize quick response times and seamless execution.</p>
    </div>
    <div class="why-card">
      <svg width="30" height="32" viewBox="0 0 30 32" fill="var(--red)"><rect x="5" y="1" width="20" height="3"/><rect x="5" y="28" width="20" height="3"/><path d="M8 4h14v4l-5 8 5 8v4H8v-4l5-8-5-8z"/><path d="M11 7h8l-4 6z M11 26l4-5 4 5z" fill="#fff"/></svg>
      <h3>Cost-Effective &amp; Efficient</h3><p>Quality service at competitive prices.</p>
    </div>
  </div>
</section>

<footer class="site-footer">
  <div class="brand"><span class="brand-mark"></span>Roadward</div>
  <div class="partner-badge" role="img" aria-label="Industry association partner badge"></div>
  <nav class="footer-nav"><span>About</span><span>Services</span><span>Rentals</span><span>Jobs</span></nav>
  <div class="footer-line"></div>
  <div class="copyright">© 2025 Roadward Lane Management Company. All rights reserved.</div>
  <div class="legal"><span>Terms</span><span>Privacy</span><span>Cookies</span></div>
</footer>

</body>
</html>
```